Brightwell Giving Inc

We need a full re-design of our non-profit organization website (www.brightwellgiving.org). Ideally, we are looking to make it more attractive, user-friendly, and interactive with our business model.

Please make sure to user colors that ago with our logo.

We need a homepage done and we also need a content page done where we will use for the other pages to fill with content.

Target Market(s)

Clothes/textiles donations.

Industry/Entity Type

Charity

Number of Pages Required

2 page

Colors

Designer to choose colors to be used in the design.

Requirements
Must have
• It must match the styling of our logo and same colors as current website. (www.brightwellgiving.org)
Nice to have
• Sleek homepage that is easy to understand and get our main points across.

```html
<!DOCTYPE html>
<html lang="en">
<head>
<meta charset="utf-8">
<title>Brightwell Giving – Home</title>
<link rel="stylesheet" href="https://fonts.googleapis.com/css2?family=Lato:ital,wght@0,400;0,700;1,400&display=swap">
<style>
:root{
  --bg:#d3efcc;
  --band:#b9e4ad;
  --green:#4f9d34;
  --green-dark:#2f7d1c;
  --ink:#1f2a1c;
  --nav-ink:#3a3a3a;
  --overlay:rgba(170,215,150,.78);
  --white:#ffffff;
}
*{margin:0;padding:0;box-sizing:border-box}
html,body{width:1200px;height:1200px;overflow:hidden}
body{background:var(--bg);font-family:"Lato",sans-serif;color:var(--ink);position:relative}

.topbar{position:absolute;left:0;top:0;width:1200px;height:46px;border-bottom:1px solid #6e8f63}
.nav{position:absolute;left:86px;top:0;display:flex;height:46px}
.nav a{display:block;font-size:13.5px;font-weight:700;color:var(--nav-ink);text-decoration:none;line-height:46px;margin-right:23px;position:relative}
.nav a.active{color:var(--green)}
.nav a.active::after{content:"";position:absolute;left:0;right:0;bottom:0;height:3px;background:var(--green)}
.contact{position:absolute;left:930px;top:0;width:172px;height:46px;background:#8cc47a;color:var(--white);font-size:11.5px;line-height:13.5px;padding:10px 0 0 30px}
.contact svg{position:absolute;left:9px;top:12px}

.masthead{position:absolute;left:0;top:47px;width:1200px;height:73px;background:var(--band)}
.brand{position:absolute;left:86px;top:13px;display:flex;align-items:center}
.brand-mark{width:18px;height:18px;background:var(--green);margin-right:10px}
.brand-name{font-size:20px;font-weight:700;color:var(--green-dark);letter-spacing:.5px;line-height:22px}
.brand-tag{position:absolute;left:86px;top:47px;font-size:11.5px;color:var(--ink)}

.hero{position:absolute;left:0;top:120px;width:1200px;height:629px;background:linear-gradient(180deg,#6d5a4a 0%,#7a604a 40%,#a27a5b 70%,#b48d6c 100%)}
.hero-caption{position:absolute;left:386px;top:383px;width:428px;height:103px;background:var(--overlay);text-align:center}
.hero-caption::before{content:"";position:absolute;left:0;top:0;width:42px;height:44px;border-left:4px solid var(--green-dark);border-top:4px solid var(--green-dark)}
.hero-caption::after{content:"";position:absolute;right:0;bottom:0;width:42px;height:44px;border-right:4px solid var(--green-dark);border-bottom:4px solid var(--green-dark)}
.hero-caption h1{font-weight:400;font-size:27px;color:var(--white);margin-top:22px}
.btn{display:inline-block;background:var(--green);color:var(--white);font-weight:700;font-size:12px;text-decoration:none}
.hero-caption .btn{padding:3px 6px;margin-top:4px}
.arrow{position:absolute;top:409px;width:51px;height:51px;border:2px solid #d5edcc;background:rgba(170,215,150,.55);display:flex;align-items:center;justify-content:center}
.arrow.prev{left:13px}.arrow.next{left:1136px}
.dots{position:absolute;display:flex;gap:6px}
.dots span{width:12px;height:12px;border:2px solid var(--band)}
.dots span.on{background:var(--band)}
.hero .dots{left:1131px;top:602px}

.news{position:absolute;left:86px;top:801px;width:1028px;height:351px;background:var(--band)}
.news h2{font-size:23px;font-weight:700;height:51px;line-height:51px;padding-left:13px}
.news-photo{position:absolute;left:0;top:51px;width:600px;height:300px;background:radial-gradient(ellipse at 55% 55%,#c7a47a 0%,#8d7350 30%,#3d4a2a 65%,#243020 100%)}
.news-body{position:absolute;left:613px;top:56px;width:392px}
.news-date{font-size:11px;font-style:italic;color:#4a5a44}
.news-title{font-size:20px;font-weight:400;line-height:24px;margin-top:2px}
.news-text{font-size:13px;line-height:16.5px;margin-top:6px}
.news-body .btn{font-weight:400;padding:6px 10px;margin-top:10px}
.news .dots{left:799px;top:338px;gap:3px}
.news .dots span{width:9px;height:9px;border-color:var(--green-dark)}
.news .dots span.on{background:var(--green-dark)}
</style>
</head>
<body>
<header class="topbar">
  <nav class="nav">
    <a class="active" href="#">Home</a>
    <a href="#">Missions</a>
    <a href="#">About us</a>
    <a href="#">How it works</a>
    <a href="#">News</a>
    <a href="#">Sponsors</a>
    <a href="#">Wall of needs</a>
  </nav>
  <div class="contact">
    <svg width="14" height="20" viewBox="0 0 14 20"><path d="M4 1 L7 5 L5 7 Q6 11 9 14 L11 12 L14 15 L11 19 Q2 15 1 4 Z" fill="#fff"/></svg>
    Toll Free: (855) 412-0968<br>New York: 518-204-3371
  </div>
</header>
<div class="masthead">
  <div class="brand"><span class="brand-mark"></span><span class="brand-name">BRIGHTWELL GIVING</span></div>
  <div class="brand-tag">Think Globally while Donating Locally</div>
</div>

<section class="hero">
  <div role="img" aria-label="Toddler sitting on a wooden porch" style="position:absolute;inset:0"></div>
  <a class="arrow prev" href="#" aria-label="Previous"><svg width="12" height="16" viewBox="0 0 12 16"><path d="M9 2 L3 8 L9 14" stroke="#fff" stroke-width="3" fill="none"/></svg></a>
  <a class="arrow next" href="#" aria-label="Next"><svg width="12" height="16" viewBox="0 0 12 16"><path d="M3 2 L9 8 L3 14" stroke="#fff" stroke-width="3" fill="none"/></svg></a>
  <div class="hero-caption">
    <h1>Helping Needy Children in Ukraine</h1>
    <a class="btn" href="#">Learn More</a>
  </div>
  <div class="dots"><span class="on"></span><span></span><span></span></div>
</section>

<section class="news">
  <h2>Charity News</h2>
  <div class="news-photo" role="img" aria-label="Girl with long hair and an orange knitted scarf"></div>
  <article class="news-body">
    <div class="news-date">March 23, 2018</div>
    <h3 class="news-title">Starting the projects to collect funds on KindFund</h3>
    <p class="news-text">Lorem ipsum dolor sit amet, consectetur adipisicing elit, sed do eiusmod tempor incididunt ut labore et dolore magna aliqua. Ut enim ad minim veniam, quis nostrud exercitation ullamco laboris nisi ut aliquip ex ea commodo consequat. Duis aute irure dolor in reprehenderit in voluptate velit esse cillum dolore eu fugiat nu ...</p>
    <a class="btn" href="#">Read More</a>
  </article>
  <div class="dots"><span></span><span class="on"></span><span></span></div>
</section>
</body>
</html>
```